Most Spectacularly Intriguing Website Ever

Alright, I'm a professional adventurer and a serial entrepreneur.
I am becoming a life coach and need an amazing website for my personal brand as an adventurer and entrepreneur as well as my life coaching.

I have previously kayaked a few major expeditions and launched a few businesses before. I want part of the website to be who I am and also what I can offer.

It needs to be amazing. Captivating. Intriguing. And most importantly make people say "I HAVE TO HIRE THIS GUY"!

You have full creative power. Use the deepest parts of your imagination. No particular colour schemes or themes in mind. So do whatever you like!

Industry/Entity Type

Life Coaching

Number of Pages Required

1 page

Requirements
Must have
• MUST be captivating, amazing, incredible.
Should not have
• Designs that are clearly just templates and stock standard mass produced designs will not be excepted. I am looking for something unique, with flare. That looks professionally made. Not like it is a template off a build your own website provider.

```html
<!DOCTYPE html>
<html lang="en">
<head>
<meta charset="utf-8">
<title>Cody Harlan — Adventurer, Entrepreneur, Life Coach</title>
<link rel="stylesheet" href="https://fonts.googleapis.com/css2?family=Kaushan+Script&family=Questrial&family=Oswald:wght@500&family=Montserrat:wght@600;700&display=swap">
<style>
:root{
  --navy:#1c3a6e;
  --navy-deep:#14305e;
  --red:#d91f33;
  --green:#8cc63e;
  --green-soft:#cde79a;
  --yellow:#f7b52a;
  --yellow-soft:#fbd46c;
  --pink:#ee86a8;
  --pink-soft:#f7c2d3;
  --teal-soft:#bfe8ec;
  --text:#7a7f88;
  --white:#fff;
}
*{margin:0;padding:0;box-sizing:border-box}
html,body{width:1200px;height:5143px;overflow:hidden}
body{position:relative;background:var(--white);font-family:'Questrial',sans-serif;color:var(--text)}
.abs{position:absolute}
.script{font-family:'Kaushan Script',cursive;color:var(--navy);line-height:1.15;white-space:nowrap}
.kicker{font-family:'Montserrat',sans-serif;font-weight:700;color:var(--red);font-size:30px;line-height:1.2}
p{font-size:15px;line-height:1.75}

/* hero */
.hero{left:0;top:0;width:1200px;height:800px;background:linear-gradient(180deg,#8fc6ec 0%,#c9e2f2 22%,#6b8d55 40%,#8ea05a 65%,#b5b377 100%)}
.hero-edge{left:0;top:700px;width:1200px;height:140px}
.menu{left:40px;top:62px;width:36px}
.menu span{display:block;height:4px;background:var(--navy-deep);margin-bottom:7px;border-radius:2px}
.brand{left:0;top:34px;width:1200px;text-align:center;font-size:96px;color:var(--navy-deep)}
.hire{left:1038px;top:66px;width:112px;height:38px;background:var(--red);color:var(--white);font-family:'Kaushan Script',cursive;font-size:20px;text-align:center;line-height:38px;transform:skew(-6deg);border-radius:3px}

/* intro */
.intro-kicker{left:0;top:940px;width:1200px;text-align:center;padding-right:150px}
.intro-title{left:0;top:978px;width:1200px;text-align:center;font-size:92px}
.service{top:1110px;width:300px;text-align:center}
.service .icon{width:80px;height:80px;margin:0 auto 20px}
.service h3{font-family:'Montserrat',sans-serif;font-weight:600;color:var(--navy);font-size:20px;margin-bottom:12px}
.service p{font-size:14px;line-height:1.7}

.peaks{left:0;top:1380px;width:1200px;height:260px;background:linear-gradient(180deg,#fff 0%,#dbe9f3 35%,#b7cfe0 55%,#e6eff6 80%,#fff 100%)}

/* about */
.portrait{left:60px;top:1640px;width:410px;height:810px;background:linear-gradient(160deg,#6b5a48 0%,#b33a3e 40%,#8b7f6e 70%,#4d4640 100%);clip-path:polygon(14% 2%,88% 0,100% 12%,96% 45%,100% 80%,86% 98%,30% 100%,4% 88%,0 40%)}
.about-title{left:548px;top:1692px;font-size:66px}
.about-title em{color:var(--red);font-style:normal}
.about-copy{left:548px;top:1780px;width:520px}
.about-copy p{font-size:14px;margin-bottom:18px;line-height:1.7}
.faq{left:548px;width:518px;height:44px;border-radius:22px;font-family:'Montserrat',sans-serif;font-weight:600;font-size:13px;color:var(--navy);line-height:44px;padding:0 26px}
.faq::after{content:"»";position:absolute;right:26px;font-size:20px;color:var(--navy)}
.faq.q1{top:2170px;background:var(--pink-soft)}
.faq.q2{top:2240px;background:var(--teal-soft)}
.faq.q3{top:2310px;background:var(--green-soft)}

/* packages */
.packages-bg{left:0;top:2480px;width:1200px;height:820px;background:linear-gradient(180deg,#fff 0%,#fdf4e7 40%,#eef4f9 80%,#fff 100%)}
.pk-kicker{left:0;top:2510px;width:1200px;text-align:center;padding-right:220px}
.pk-title{left:0;top:2548px;width:1200px;text-align:center;font-size:92px}
.card{top:2720px;width:272px;height:400px;border-radius:6px;box-shadow:0 10px 24px rgba(0,0,0,.12);overflow:hidden}
.card h3{height:100px;padding-top:26px;text-align:center;font-family:'Oswald',sans-serif;font-weight:500;font-size:24px;line-height:1.1;color:var(--navy)}
.card ul{list-style:none;padding:10px 24px 0}
.card li{font-size:13px;color:var(--white);padding:9px 0 9px 26px;border-bottom:1px solid rgba(255,255,255,.35);position:relative}
.card li::before{content:"";position:absolute;left:2px;top:10px;width:10px;height:6px;border-left:3px solid var(--navy);border-bottom:3px solid var(--navy);transform:rotate(-45deg)}
.card .join{position:absolute;left:86px;bottom:26px;width:100px;height:36px;line-height:36px;text-align:center;color:var(--white);font-family:'Kaushan Script',cursive;font-size:18px;border-radius:3px}
.card.aerial{left:130px;background:var(--green)}
.card.aerial h3{background:var(--green-soft)}
.card.aerial .join{background:#6c9c2a}
.card.rafting{left:465px;background:var(--yellow)}
.card.rafting h3{background:var(--yellow-soft)}
.card.rafting .join{background:var(--red)}
.card.custom{left:802px;background:var(--pink)}
.card.custom h3{background:var(--pink-soft)}
.card.custom .join{background:#d94d7d}

/* adventures */
.adv-kicker{left:0;top:3380px;width:1200px;text-align:center;padding-right:120px}
.adv-title{left:0;top:3414px;width:1200px;text-align:center;font-size:92px}
.photo{background:#fff;padding:12px;box-shadow:0 6px 18px rgba(0,0,0,.2)}
.photo div{width:100%;height:100%}
.ph1{left:200px;top:3560px;width:180px;height:150px;transform:rotate(-8deg)}
.ph1 div{background:linear-gradient(160deg,#5a8ac2,#7ea86a)}
.ph2{left:130px;top:3650px;width:280px;height:320px;transform:rotate(-6deg)}
.ph2 div{background:linear-gradient(180deg,#3c7fd2 0%,#c9663a 55%,#9c4a2a 100%)}
.ph3{left:300px;top:3630px;width:270px;height:330px;transform:rotate(7deg)}
.ph3 div{background:linear-gradient(180deg,#eaf3fb 0%,#8fb2c7 45%,#5a7351 100%)}
.adv-name{left:665px;top:3585px;font-family:'Montserrat',sans-serif;font-weight:700;font-size:30px;color:var(--green)}
.adv-copy{left:665px;top:3650px;width:440px}
.adv-copy p{font-size:14px;line-height:1.7}
.btn-red{left:665px;top:3850px;width:130px;height:40px;line-height:40px;text-align:center;background:var(--red);color:var(--white);font-family:'Kaushan Script',cursive;font-size:19px;border-radius:3px}
.arrow{top:3680px;width:40px;height:80px}

/* stories */
.stories-bg{left:0;top:4060px;width:1200px;height:420px;background:linear-gradient(180deg,#fff 0%,#e8f0f8 30%,#e3edf6 70%,#fff 100%)}
.st-kicker{left:240px;top:4205px}
.st-title{left:130px;top:4240px;font-size:104px}
.divider{left:410px;top:4200px;width:2px;height:190px;background:#cbd8e5}
.avatar{left:465px;top:4205px;width:134px;height:134px;border-radius:50%;border:5px solid var(--green);background:linear-gradient(180deg,#e6a074,#5b3a2a)}
.quote{left:650px;top:4200px;width:470px}
.quote p{font-size:14px;line-height:1.7}
.quote .who{font-family:'Montserrat',sans-serif;font-weight:700;color:var(--red);font-size:12px;margin-top:10px}
.quote-mark{left:1050px;top:4330px;font-family:'Montserrat',sans-serif;font-size:90px;color:#ccd6df;line-height:1}

/* newsletter */
.nl-kicker{left:0;top:4500px;width:1200px;text-align:center;padding-left:60px}
.nl-title{left:0;top:4536px;width:1200px;text-align:center;font-size:96px}
.field{left:275px;top:4718px;width:620px;height:52px;border:2px dashed #e3a0ab;background:#fbf8f9;padding-left:26px;line-height:48px;color:var(--navy);font-size:15px}
.subscribe{left:808px;top:4726px;width:140px;height:38px;line-height:38px;text-align:center;background:var(--red);color:var(--white);font-family:'Kaushan Script',cursive;font-size:19px;border-radius:3px}

/* footer */
.ghost{left:0;top:4895px;width:1200px;text-align:center;font-size:90px;color:#dfe6ef}
.footer{left:0;top:4975px;width:1200px;height:168px;background:var(--navy-deep)}
.foot-nav{left:130px;top:5005px;display:flex}
.foot-nav a{color:#e2e9f5;text-decoration:none;font-size:16px;margin-right:48px}
.foot-line{left:130px;top:5062px;width:940px;height:1px;background:rgba(255,255,255,.2)}
.copyright{left:130px;top:5090px;color:#c4cfe2;font-size:14px}
.social{left:860px;top:5086px;display:flex;gap:22px}
.social span{width:26px;height:26px;border-radius:50%;border:2px solid #e2e9f5}
</style>
</head>
<body>

<div class="abs hero" role="img" aria-label="Photo of Cody kneeling on a grassy plain among kangaroos, hills and blue sky behind"></div>
<svg class="abs hero-edge" viewBox="0 0 1200 140" preserveAspectRatio="none" aria-hidden="true">
  <path d="M0 40 L60 70 L120 35 L200 80 L270 50 L340 95 L420 60 L500 100 L560 70 L640 110 L720 75 L790 105 L860 65 L940 95 L1010 55 L1090 85 L1150 45 L1200 60 L1200 140 L0 140 Z" fill="#fff"/>
</svg>
<div class="abs menu" aria-label="Menu"><span></span><span></span><span></span></div>
<div class="abs brand script">Cody Harlan</div>
<div class="abs hire">Hire Me</div>

<div class="abs intro-kicker kicker">You Have One Life</div>
<div class="abs intro-title script">make it epic</div>

<div class="abs service" style="left:125px">
  <svg class="icon" viewBox="0 0 80 80" aria-hidden="true"><circle cx="40" cy="40" r="30" fill="none" stroke="#ee86a8" stroke-width="3"/><circle cx="40" cy="40" r="22" fill="none" stroke="#ee86a8" stroke-width="2"/><path d="M48 30 L43 43 L32 50 L37 37 Z" fill="#ee86a8"/></svg>
  <h3>Adventurer</h3>
  <p>Cody spent much of his childhood in the outdoors and bush walking, learning much about the rugged bush.</p>
</div>
<div class="abs service" style="left:450px">
  <svg class="icon" viewBox="0 0 80 80" aria-hidden="true"><path d="M33 10 H47 L44 20 L52 58 L40 72 L28 58 L36 20 Z" fill="none" stroke="#f7b52a" stroke-width="3" stroke-linejoin="round"/><path d="M36 20 H44" stroke="#f7b52a" stroke-width="3"/></svg>
  <h3>Entrepreneur</h3>
  <p>Cody spent much of his childhood in the outdoors and bush walking, learning much about the rugged bush.</p>
</div>
<div class="abs service" style="left:775px">
  <svg class="icon" viewBox="0 0 80 80" aria-hidden="true"><rect x="36" y="14" width="34" height="24" fill="none" stroke="#8cc63e" stroke-width="3"/><circle cx="20" cy="24" r="7" fill="none" stroke="#8cc63e" stroke-width="3"/><path d="M20 31 V54 M20 38 L36 28 M20 54 L12 72 M20 54 L28 72" stroke="#8cc63e" stroke-width="3" fill="none"/><path d="M6 72 H74" stroke="#8cc63e" stroke-width="3"/></svg>
  <h3>Life Coaching</h3>
  <p>Cody spent much of his childhood in the outdoors and bush walking, learning much about the rugged bush.</p>
</div>

<div class="abs peaks" role="img" aria-label="Misty snow-capped mountain range"></div>

<div class="abs portrait" role="img" aria-label="Photo of Cody in a hat and red shirt leaning on a weathered timber post"></div>
<div class="abs about-title script">Hi, <em>I'm Cody</em></div>
<div class="abs about-copy">
  <p>Cody spent much of his childhood in the outdoors and bush walking, learning much about the wild bush. Throughout his early teens, Cody developed a keen interest in wildlife and photography, frequently catching all sorts of bugs and reptiles along the way.</p>
  <p>At the age of 16 Cody embarked on his first adventure and hitch hiked over 4,000 km across the country, filming his experience along the way. Cody spent most of his time doing micro adventures around the coast and filming a survival show called Outback Trails. Cody also spent 3 years as a volunteer keeper and tour guide at Ridgeway Bird Park.</p>
  <p>In December 2017, Cody was nominated for and won an Adventurer of the Month award for his previous adventures and future ambitions to become the youngest person to kayak the full length of the Murray River.</p>
</div>
<div class="abs faq q1">Q1. Why should I sign up for Adventure Coaching?</div>
<div class="abs faq q2">Q2. How is Adventure Coaching different from the rest?</div>
<div class="abs faq q3">Q3. What is an Adventure Coach?</div>

<div class="abs packages-bg"></div>
<div class="abs pk-kicker kicker">Coaching</div>
<div class="abs pk-title script">packages</div>

<div class="abs card aerial">
  <h3>AERIAL<br>ADVENTURE</h3>
  <ul><li>Flight over the coast</li><li>Full day of guiding</li><li>Five hours airborne</li><li>Leap into open skies</li><li>Photos of your trip</li><li>Meals and drinks</li></ul>
  <div class="join">Join Now</div>
</div>
<div class="abs card rafting">
  <h3>RAFTING<br>ADVENTURE</h3>
  <ul><li>Three days on river</li><li>Full gear provided</li><li>Five rapid sections</li><li>Leap into deep pools</li><li>Photos of your trip</li><li>Camp by the water</li></ul>
  <div class="join">Join Now</div>
</div>
<div class="abs card custom">
  <h3>CUSTOM<br>ADVENTURE</h3>
  <ul><li>Plan your own route</li><li>One on one coaching</li><li>Five goal sessions</li><li>Leap into new places</li><li>Photos of your trip</li><li>Ongoing mentoring</li></ul>
  <div class="join">Join Now</div>
</div>

<div class="abs adv-kicker kicker">Previous</div>
<div class="abs adv-title script">adventures</div>
<div class="abs photo ph1"><div role="img" aria-label="Photo of a group of hikers on a hillside"></div></div>
<div class="abs photo ph2"><div role="img" aria-label="Photo of a red sandstone arch under blue sky"></div></div>
<div class="abs photo ph3"><div role="img" aria-label="Photo of friends walking along a mountain trail"></div></div>
<div class="abs adv-name">The Murray River</div>
<div class="abs adv-copy"><p>At the age of 16 Cody embarked on his first adventure and hitch hiked over 4,000 km across the country, filming his experience along the way. Cody spent most of his time doing micro adventures around the coast and filming a survival show called Outback Trails. Cody also spent 3 years as a volunteer bird keeper and tour guide at Ridgeway Bird Park.</p></div>
<div class="abs btn-red">Read More</div>
<svg class="abs arrow" style="left:40px" viewBox="0 0 40 80" aria-hidden="true"><path d="M32 6 L8 40 L32 74" fill="none" stroke="#c9d3de" stroke-width="3"/></svg>
<svg class="abs arrow" style="left:1120px" viewBox="0 0 40 80" aria-hidden="true"><path d="M8 6 L32 40 L8 74" fill="none" stroke="#c9d3de" stroke-width="3"/></svg>

<div class="abs stories-bg"></div>
<div class="abs st-kicker kicker">Success</div>
<div class="abs st-title script">Stories</div>
<div class="abs divider"></div>
<div class="abs avatar" role="img" aria-label="Portrait photo of a client"></div>
<div class="abs quote">
  <p>Working with Cody changed how I set goals and chase them. His coaching pushed me out of my comfort zone and into the outdoors, and I came home with a clear plan for my business and for my life. I recommend his programs to anyone ready for real change.</p>
  <div class="who">Megan Lowry</div>
</div>
<div class="abs quote-mark">&#8221;</div>
<svg class="abs" style="left:1130px;top:4250px" width="20" height="40" viewBox="0 0 20 40" aria-hidden="true"><path d="M4 4 L16 20 L4 36" fill="none" stroke="#c9d3de" stroke-width="3"/></svg>

<div class="abs nl-kicker kicker">Newsletter</div>
<div class="abs nl-title script">Sign up</div>
<div class="abs field">Enter Your Email</div>
<div class="abs subscribe">Subscribe</div>

<div class="abs ghost script">Cody Harlan</div>
<div class="abs footer"></div>
<nav class="abs foot-nav">
  <a>Life Coaching</a><a>Previous Adventure</a><a>Leadership</a><a>Success Stories</a><a>Blog</a><a>About</a><a>Contact</a>
</nav>
<div class="abs foot-line"></div>
<div class="abs copyright">Copyright © 2017 Cody Harlan.</div>
<div class="abs social" aria-label="Social links"><span></span><span></span><span></span><span></span><span></span></div>

</body>
</html>
```